Project Managers Business card design

We need business cards for our Project Managers based in Sydney for our business name Korbet Pty Ltd. We project manage property improvements and infrastructure Assets. We provide asset owners Project Management services from original concept, management of architectural and engineering designs, call and select construction tenders, and manage the Asset operational life cycle to conclusion and removal. We are experienced in feasibility studies, risk assessments, quality control, safety control, environmental analysis. We are specialist in Aged Care and Child Care Services. We can provide asset reviewing checklists, asset inspections, contract cost and contract assessments, dispute resolution services and articles and books on safely working and living in environments subject to analysis. the design colours should be queensland marone and NSW sky blue.

Industry/Entity Type

Construction

Contact Information for Business Card

Dennis Marlow (Mb 0402 781954), Gavin Trelford (Mb 0438 216 047), Len Obradin,(Mb 0427 863 105)
E: all business cards: korbet@mailnest.example
Office phone number (02) 9482 3061
Address
Level 1 Harwell Building
47 Fenwick Street, Parramatta
Web: projectmanagers@estateleadsbykorbet.example (to be checked on Printwell web draft)

```html
<!DOCTYPE html>
<html lang="en">
<head>
<meta charset="utf-8">
<title>Korbet Pty Ltd – Business Cards</title>
<link rel="stylesheet" href="https://fonts.googleapis.com/css2?family=Cinzel:wght@400&family=Crimson+Text:wght@400;600&family=Open+Sans:wght@400&display=swap">
<style>
  :root {
    --bg: #ece9e4;
    --card-white: #fbfbfb;
    --maroon: #8e1b20;
    --maroon-dark: #6a0f13;
    --maroon-light: #a8282d;
    --ink: #2b2b2b;
    --text-grey: #555555;
    --rule: #3a3a3a;
    --on-maroon: #ffffff;
  }
  * { margin: 0; padding: 0; box-sizing: border-box; }
  html, body { width: 1200px; height: 1023px; overflow: hidden; }
  body {
    background: var(--bg);
    display: flex;
    flex-direction: column;
    align-items: center;
    justify-content: center;
    gap: 60px;
    font-family: "Open Sans", Arial, sans-serif;
  }
  .card {
    width: 620px;
    height: 370px;
    border-radius: 16px;
    position: relative;
    overflow: hidden;
    box-shadow: 0 6px 18px rgba(0,0,0,0.18);
  }

  /* Front */
  .card-front { background: var(--card-white); }
  .brand {
    position: absolute;
    top: 64px;
    right: 44px;
    display: flex;
    align-items: center;
    gap: 16px;
  }
  .brand-dot {
    width: 44px; height: 44px;
    border-radius: 50%;
    background: var(--maroon);
  }
  .brand-name {
    font-family: "Cinzel", Georgia, serif;
    font-weight: 400;
    font-size: 34px;
    color: var(--ink);
    letter-spacing: 1px;
    white-space: nowrap;
  }
  .divider {
    position: absolute;
    left: 0; right: 0;
    top: 160px;
    border-top: 1.5px solid var(--rule);
  }
  .divider-tick {
    position: absolute;
    left: 252px;
    top: 160px;
    height: 210px;
    border-left: 1.5px solid var(--rule);
  }
  .person-name {
    position: absolute;
    left: 32px;
    top: 184px;
    font-family: "Cinzel", Georgia, serif;
    font-weight: 400;
    font-size: 19px;
    color: var(--maroon);
    letter-spacing: 1px;
    white-space: nowrap;
  }
  .contact-list {
    position: absolute;
    left: 32px;
    top: 236px;
    list-style: none;
    display: flex;
    flex-direction: column;
    gap: 12px;
  }
  .contact-item {
    display: flex;
    align-items: center;
    gap: 10px;
    font-size: 13.5px;
    color: var(--text-grey);
    white-space: nowrap;
  }
  .contact-icon { width: 20px; height: 20px; flex: none; }
  .address {
    position: absolute;
    left: 272px;
    top: 184px;
    font-size: 14px;
    font-style: normal;
    line-height: 1.8;
    color: var(--ink);
    white-space: nowrap;
  }
  .web {
    display: flex;
    align-items: center;
    gap: 8px;
    margin-top: 4px;
    font-size: 12px;
    color: var(--text-grey);
  }

  /* Back */
  .card-back {
    background: linear-gradient(135deg, var(--maroon-light) 0%, var(--maroon) 45%, var(--maroon-dark) 100%);
    color: var(--on-maroon);
    padding: 34px 40px;
  }
  .back-brand {
    font-family: "Cinzel", Georgia, serif;
    font-weight: 400;
    font-size: 30px;
    letter-spacing: 1px;
  }
  .services-heading {
    font-family: "Crimson Text", Georgia, serif;
    font-weight: 600;
    font-size: 20px;
    line-height: 1.3;
    margin-top: 24px;
  }
  .services-list {
    list-style: none;
    margin-top: 16px;
    display: flex;
    flex-direction: column;
    gap: 6px;
    font-size: 13px;
  }
  .services-list li { white-space: nowrap; }
  .services-list li::before {
    content: "";
    display: inline-block;
    width: 7px; height: 7px;
    border-radius: 50%;
    background: var(--on-maroon);
    margin-right: 10px;
    vertical-align: middle;
  }
</style>
</head>
<body>

<section class="card card-front" aria-label="Business card front">
  <div class="brand">
    <span class="brand-dot"></span>
    <span class="brand-name">KORBET PTY LTD.</span>
  </div>
  <div class="divider"></div>
  <div class="divider-tick"></div>

  <h1 class="person-name">DENNIS MARLOW</h1>
  <ul class="contact-list">
    <li class="contact-item">
      <svg class="contact-icon" viewBox="0 0 20 20"><circle cx="10" cy="10" r="10" fill="var(--maroon)"/><rect x="7" y="4.5" width="6" height="11" rx="1" fill="none" stroke="#fff" stroke-width="1.3"/></svg>
      0402 781954
    </li>
    <li class="contact-item">
      <svg class="contact-icon" viewBox="0 0 20 20"><circle cx="10" cy="10" r="10" fill="var(--maroon)"/><path d="M6.5 5.5c1-.6 1.6 0 2.2 1.3.4.8 0 1.2-.5 1.6.5 1.3 1.4 2.3 2.7 2.9.4-.5.9-.9 1.6-.5 1.3.6 1.9 1.2 1.3 2.2-.8 1.3-2.3 1.2-3.9.3-1.9-1.1-3.4-2.9-4.1-4.9-.4-1.3-.2-2.4.7-2.9z" fill="#fff"/></svg>
      (02) 9482 3061
    </li>
    <li class="contact-item">
      <svg class="contact-icon" viewBox="0 0 20 20"><circle cx="10" cy="10" r="10" fill="var(--maroon)"/><rect x="5" y="6.5" width="10" height="7" fill="none" stroke="#fff" stroke-width="1.2"/><path d="M5 6.5l5 4 5-4" fill="none" stroke="#fff" stroke-width="1.2"/></svg>
      korbet@mailnest.example
    </li>
  </ul>

  <address class="address">
    Level 1 Harwell Building<br>
    47 Fenwick Street, Parramatta
    <span class="web">
      <svg class="contact-icon" viewBox="0 0 20 20"><circle cx="10" cy="10" r="10" fill="var(--maroon)"/><circle cx="10" cy="10" r="5.5" fill="none" stroke="#fff" stroke-width="1"/><ellipse cx="10" cy="10" rx="2.4" ry="5.5" fill="none" stroke="#fff" stroke-width="1"/><path d="M4.5 10h11" stroke="#fff" stroke-width="1"/></svg>
      projectmanagers@estateleadsbykorbet.example
    </span>
  </address>
</section>

<section class="card card-back" aria-label="Business card back">
  <h2 class="back-brand">KORBET PTY LTD.</h2>
  <p class="services-heading">Korbet offers our Trusted Partners<br>the following Property Asset Management Services:</p>
  <ul class="services-list">
    <li>Building and Property Planning, Feasibility, Development and consulting advice</li>
    <li>Project Management</li>
    <li>Construction Management</li>
    <li>Operating and Maintaining facilities</li>
  </ul>
</section>

</body>
</html>
```